Web design

We need the design for the logo and website for a women fashion website. No coding required. The colors used should be neutral (maybe with a light touch of color), the style should be modern, slightly luxurious, not too crowded. The target market is young professionals who love trendy clothes.

Target Market(s)

Young professionals

Industry/Entity Type

Apparel

Number of Pages Required

5+ page

Font styles to use
Sans Serif
Other font styles liked:
• Montserrat, Engravers Gothic, Benton Sans, gotham-book

Colors

Designer to choose colors to be used in the design.

```html
<!DOCTYPE html>
<html lang="en">
<head>
<meta charset="utf-8">
<title>LUMA – Checkout Confirmation</title>
<link rel="stylesheet" href="https://fonts.googleapis.com/css2?family=Lato:wght@400;700&family=Montserrat:wght@400;500;600&display=swap">
<style>
  :root {
    --ink: #23232b;
    --text: #3a3a3a;
    --muted: #bdbdbd;
    --step-grey: #dedede;
    --gold: #d4a20a;
    --gold-soft: #efcf6f;
    --sale: #e8323c;
    --teal: #7fcdc1;
    --rule: #dcdcdc;
    --blush: #fdeef1;
    --button: #333333;
    --footer: #f4f3f1;
    --white: #ffffff;
  }
  * { box-sizing: border-box; margin: 0; padding: 0; }
  html, body { width: 1200px; height: 1101px; overflow: hidden; background: var(--white); }
  body { position: relative; font-family: "Montserrat", sans-serif; color: var(--text); }
  .abs { position: absolute; }

  /* Header */
  .site-header { position: absolute; left: 0; top: 0; width: 1200px; height: 76px; border-bottom: 1px solid #e6e6e6; }
  .main-nav a { position: absolute; top: 31px; font-family: "Lato", sans-serif; font-size: 14.5px; color: #222; text-decoration: none; white-space: nowrap; }
  .main-nav .sale { color: var(--sale); }
  .brand { position: absolute; font-family: "Montserrat", sans-serif; font-weight: 500; color: var(--ink); letter-spacing: 1px; white-space: nowrap; }
  .header-brand { left: 0; width: 1200px; text-align: center; top: 22px; font-size: 30px; }
  .utility { position: absolute; top: 28px; display: flex; align-items: center; }
  .lang { font-family: "Lato", sans-serif; font-size: 12px; color: #222; }
  .cart-badge { position: absolute; left: 1085px; top: 40px; width: 13px; height: 13px; border-radius: 50%; background: var(--gold); color: #fff; font-size: 8px; line-height: 13px; text-align: center; font-family: "Lato", sans-serif; }

  /* Checkout */
  .page-title { position: absolute; left: 0; width: 1200px; top: 134px; text-align: center; font-size: 43px; font-weight: 600; color: var(--ink); letter-spacing: 1px; }
  .step-num { position: absolute; top: 215px; width: 41px; height: 41px; border-radius: 50%; background: var(--step-grey); color: #fff; font-family: "Lato", sans-serif; font-size: 22px; line-height: 41px; text-align: center; }
  .step-num.active { background: var(--gold); }
  .step-label { position: absolute; top: 227px; font-family: "Lato", sans-serif; font-size: 14px; color: var(--muted); white-space: nowrap; }
  .step-label.active { color: #111; }
  .step-dash { position: absolute; top: 234px; width: 23px; height: 1px; background: var(--gold-soft); }

  .section-title { position: absolute; left: 198px; top: 322px; font-size: 30px; font-weight: 600; color: #111; letter-spacing: .5px; }
  .section-rule { position: absolute; left: 200px; top: 367px; width: 799px; height: 1px; background: var(--rule); }
  .section-rule::before { content: ""; position: absolute; left: 0; top: 0; width: 284px; height: 1px; background: var(--teal); }

  .notice { position: absolute; left: 200px; top: 406px; width: 800px; height: 84px; background: var(--blush); }
  .notice p { position: absolute; left: 120px; top: 30px; font-size: 20.5px; color: #222; white-space: nowrap; letter-spacing: .3px; }

  .receipt { position: absolute; left: 0; width: 1200px; text-align: center; color: #555; white-space: nowrap; }
  .receipt.line1 { top: 521px; font-size: 18px; letter-spacing: .3px; }
  .receipt.line1 a { color: var(--gold); text-decoration: none; }
  .receipt.line2 { top: 547px; font-size: 18px; }
  .receipt.line2 .num { font-size: 23px; letter-spacing: .5px; }

  .btn-home { position: absolute; left: 480px; top: 626px; width: 257px; height: 51px; background: var(--button); color: #fff; font-family: "Lato", sans-serif; font-weight: 700; font-size: 18px; line-height: 51px; text-align: center; text-decoration: none; letter-spacing: -.2px; }

  /* Footer */
  .site-footer { position: absolute; left: 0; top: 768px; width: 1195px; height: 333px; background: var(--footer); }
  .footer-brand { left: 95px; top: 80px; font-size: 53px; }
  .footer-col h3 { position: absolute; font-size: 16px; font-weight: 600; color: #111; letter-spacing: .8px; }
  .footer-col ul { position: absolute; list-style: none; }
  .footer-col li { height: 26.6px; font-size: 13.5px; color: #333; letter-spacing: .3px; }
  .contact-mail { position: absolute; left: 958px; top: 104px; display: flex; align-items: center; gap: 8px; font-size: 13.5px; color: #333; }
  .socials { position: absolute; left: 952px; top: 176px; display: flex; gap: 4px; }
  .socials a { width: 33px; height: 33px; border: 1px solid #222; border-radius: 50%; display: flex; align-items: center; justify-content: center; }
  .footer-rule { position: absolute; left: 106px; top: 268px; width: 976px; height: 1px; background: #cfcfcf; }
  .copyright { position: absolute; left: 0; top: 293px; width: 1200px; text-align: center; font-size: 13.5px; color: #333; letter-spacing: .2px; }
</style>
</head>
<body>

<header class="site-header">
  <nav class="main-nav">
    <a href="#" style="left:100px">Latest Arrivals</a>
    <a href="#" style="left:217px">Clothes <svg width="8" height="6" viewBox="0 0 8 6"><path d="M1 1l3 3 3-3" fill="none" stroke="#222" stroke-width="1.2"/></svg></a>
    <a href="#" style="left:308px">LUMA Club</a>
    <a href="#" class="sale" style="left:412px">On Sale</a>
  </nav>
  <div class="brand header-brand">LUMA</div>

  <svg class="abs" style="left:918px;top:32px" width="17" height="17" viewBox="0 0 17 17" aria-label="Search"><circle cx="7" cy="7" r="6" fill="none" stroke="#222" stroke-width="1.4"/><path d="M11.5 11.5L16 16" stroke="#222" stroke-width="1.4"/></svg>
  <div class="utility" style="left:963px"><span class="lang">ENG</span>
    <svg style="margin-left:4px" width="8" height="6" viewBox="0 0 8 6"><path d="M1 1l3 3 3-3" fill="none" stroke="#222" stroke-width="1.2"/></svg></div>
  <svg class="abs" style="left:1009px;top:30px" width="23" height="21" viewBox="0 0 23 21" aria-label="Wishlist"><path d="M11.5 19.5C5 14 1 10.5 1 6.3 1 3.3 3.3 1 6.2 1c2.2 0 4 1.3 5.3 3 1.3-1.7 3.1-3 5.3-3C19.7 1 22 3.3 22 6.3c0 4.2-4 7.7-10.5 13.2z" fill="none" stroke="#222" stroke-width="1.4"/></svg>
  <svg class="abs" style="left:1042px;top:28px" width="21" height="24" viewBox="0 0 21 24" aria-label="Account"><circle cx="10.5" cy="6.5" r="5.5" fill="none" stroke="#222" stroke-width="1.4"/><path d="M1 23c0-5.5 4.2-9 9.5-9s9.5 3.5 9.5 9" fill="none" stroke="#222" stroke-width="1.4"/></svg>
  <svg class="abs" style="left:1073px;top:28px" width="20" height="24" viewBox="0 0 20 24" aria-label="Bag"><path d="M1.5 8h17l-1 15h-15z" fill="none" stroke="#222" stroke-width="1.4"/><path d="M6 8V5.5a4 4 0 0 1 8 0V8" fill="none" stroke="#222" stroke-width="1.4"/></svg>
  <span class="cart-badge">0</span>
</header>

<main>
  <h1 class="page-title">CHECKOUT</h1>

  <div class="step-num" style="left:186px">1</div>
  <span class="step-label" style="left:243px">BILLING DETAILS</span>
  <span class="step-dash" style="left:367px"></span>
  <div class="step-num" style="left:400px">2</div>
  <span class="step-label" style="left:456px">SHIPPING DETAILS</span>
  <span class="step-dash" style="left:593px"></span>
  <div class="step-num" style="left:626px">3</div>
  <span class="step-label" style="left:682px">REVIEW &amp; PAYMENT</span>
  <span class="step-dash" style="left:826px"></span>
  <div class="step-num active" style="left:860px">4</div>
  <span class="step-label active" style="left:916px">CONIRMATION</span>

  <h2 class="section-title">CONFIRMATION</h2>
  <div class="section-rule"></div>

  <div class="notice"><p>YOUR ORDER HAS BEEN SUCCESSFULLY SENT! THANK YOU!</p></div>

  <p class="receipt line1">An information e-mail containing your recipt has been send to <a href="#">info@luma-style.com</a></p>
  <p class="receipt line2">Order Number <span class="num">888 888 8888</span></p>

  <a href="#" class="btn-home">BACK TO HOMEPAGE</a>
</main>

<footer class="site-footer">
  <div class="brand footer-brand">LUMA</div>

  <div class="footer-col">
    <h3 style="left:440px;top:77px">HELP</h3>
    <ul style="left:439px;top:116px">
      <li>Terms &amp; Conditions</li><li>Privacy Policy</li><li>Returns/exchanges</li><li>Delivery Information</li><li>FAQ</li>
    </ul>
  </div>
  <div class="footer-col">
    <h3 style="left:731px;top:77px">SHOP</h3>
    <ul style="left:731px;top:116px">
      <li>Tops</li><li>Bootoms</li><li>Intimates</li><li>Dresses</li><li>Swim</li>
    </ul>
  </div>
  <div class="footer-col">
    <h3 style="left:956px;top:77px">CONTACT US</h3>
    <div class="contact-mail">
      <svg width="15" height="11" viewBox="0 0 15 11" aria-label="Email"><rect x=".5" y=".5" width="14" height="10" fill="#333"/><path d="M.5.5l7 5.5 7-5.5M.5 10.5l5-4.5M14.5 10.5l-5-4.5" fill="none" stroke="#f4f3f1" stroke-width="1"/></svg>
      <span>info@luma-style.com</span>
    </div>
    <h3 style="left:956px;top:146px">FOLLOW US</h3>
    <div class="socials">
      <a href="#" aria-label="Social link 1"><svg width="10" height="10" viewBox="0 0 10 10"><path d="M2 8L8 2M3.5 2H8v4.5" fill="none" stroke="#222" stroke-width="1.3"/></svg></a>
      <a href="#" aria-label="Social link 2"><svg width="10" height="10" viewBox="0 0 10 10"><path d="M2 8L8 2M3.5 2H8v4.5" fill="none" stroke="#222" stroke-width="1.3"/></svg></a>
      <a href="#" aria-label="Social link 3"><svg width="10" height="10" viewBox="0 0 10 10"><path d="M2 8L8 2M3.5 2H8v4.5" fill="none" stroke="#222" stroke-width="1.3"/></svg></a>
      <a href="#" aria-label="Social link 4"><svg width="10" height="10" viewBox="0 0 10 10"><path d="M2 8L8 2M3.5 2H8v4.5" fill="none" stroke="#222" stroke-width="1.3"/></svg></a>
    </div>
  </div>

  <div class="footer-rule"></div>
  <p class="copyright">Terms &amp; Conditions, Privacy Policy and @2021 followed by luma.</p>
</footer>

</body>
</html>
```